Building company buisness cards

We are looking for a sharp modern new look for our business cards.
We are a New Zealand based company that specialises in house and land packages.
We have attached a photo of the current logo and would like to see if it can be improved somehow if needed.
We are open to any colours but we have chosen green at this stage.
Feel free to change the font and make the logo smarter looking.
Play with the colours and see what looks best.

We want a card that looks so good know one will want to throw it away!

Target Market(s)

Home buyers

Industry/Entity Type

Building

Contact Information for Business Card

Dorian Keswick
0217392604
dkeswick@tidewellhomecraft.co.nz
tidewellhomecraft.co.nz

Font styles to use
Serif
Sans Serif

Colors

Designer to choose colors to be used in the design.

Requirements
Must have
• Logo and company name on one side, details on the other side
Nice to have
• Color codes for the original green are HEX #4a8028, RGB(74,128,40), CMYK(42,0,69,50)
• Round corners, Raised and/or spot UV

```html
<!DOCTYPE html>
<html lang="en">
<head>
<meta charset="utf-8">
<title>Tidewell Homecraft — Business Cards</title>
<link rel="stylesheet" href="https://fonts.googleapis.com/css2?family=Source+Sans+3:wght@400;600;700;900&display=swap">
<style>
  :root {
    --bg: #2a2b2d;
    --green: #4a8028;
    --green-light: #8ee64c;
    --green-mid: #5fa532;
    --grey: #5a5a5a;
    --white: #ffffff;
    --ink: #ffffff;
  }
  * { box-sizing: border-box; margin: 0; padding: 0; }
  html, body {
    width: 1200px; height: 885px; overflow: hidden;
    background: var(--bg);
    font-family: "Source Sans 3", sans-serif;
  }
  .canvas { position: relative; width: 1200px; height: 885px; }
  .card {
    position: absolute; width: 600px; height: 343px;
    border-radius: 6px; overflow: hidden;
    box-shadow: 0 18px 40px rgba(0,0,0,.45);
  }
  .card--front {
    left: 80px; top: 70px;
    background: linear-gradient(135deg, var(--green-light) 0%, var(--green-mid) 45%, var(--green) 100%);
    display: flex; align-items: center; justify-content: center;
  }
  .brand-mark {
    display: flex; align-items: center; gap: 14px;
    color: var(--ink); font-weight: 900; font-size: 40px; letter-spacing: -0.5px;
  }
  .brand-mark__dot {
    width: 22px; height: 22px; border-radius: 50%; background: var(--ink);
  }
  .card--back { left: 520px; top: 470px; background: var(--white); }
  .back__wordmark {
    position: absolute; left: 0; right: 0; top: 80px;
    text-align: center; color: var(--green);
    font-weight: 900; font-size: 38px; line-height: 1; letter-spacing: -0.5px;
  }
  .back__rule {
    position: absolute; left: 270px; width: 60px; top: 132px;
    height: 1px; background: #d8d8d8;
  }
  .back__stripe {
    position: absolute; left: 0; right: 0; top: 205px; height: 9px; background: var(--grey);
  }
  .back__notch { position: absolute; left: 128px; top: 213px; }
  .back__band {
    position: absolute; left: 0; right: 0; top: 214px; bottom: 0; background: var(--green);
  }
  .contact {
    position: absolute; left: 330px; top: 230px;
    list-style: none; color: var(--ink); font-size: 15px; line-height: 22px;
  }
  .contact__item { display: flex; align-items: center; gap: 8px; }
  .contact__item svg { width: 14px; height: 14px; flex: none; }
  .holder-name {
    position: absolute; left: 34px; bottom: 24px;
    color: var(--ink); font-weight: 700; font-size: 24px; letter-spacing: .3px;
    text-transform: uppercase;
  }
</style>
</head>
<body>
<main class="canvas">

  <section class="card card--front" aria-label="Card front">
    <div class="brand-mark">
      <span class="brand-mark__dot"></span>
      <span>tidewell homecraft</span>
    </div>
  </section>

  <section class="card card--back" aria-label="Card back">
    <div class="back__wordmark">tidewell homecraft.</div>
    <div class="back__rule"></div>
    <div class="back__band"></div>
    <div class="back__stripe"></div>
    <svg class="back__notch" width="36" height="18" viewBox="0 0 36 18" aria-hidden="true">
      <polygon points="0,0 36,0 18,18" fill="var(--grey)"/>
    </svg>

    <ul class="contact">
      <li class="contact__item">
        <svg viewBox="0 0 16 16" aria-hidden="true"><path fill="#fff" d="M3.6 1.2l2.2 2.6-1.3 1.6c.9 2 2.3 3.4 4.2 4.3l1.6-1.3 2.5 2.2-1.3 2.5C6.6 13 3 9.4 1.2 4.5z"/></svg>
        <span>0217392604</span>
      </li>
      <li class="contact__item">
        <svg viewBox="0 0 16 16" aria-hidden="true"><rect x="1" y="3.5" width="14" height="9" rx="1" fill="#fff"/><path d="M1.5 4l6.5 5 6.5-5" stroke="var(--green)" stroke-width="1.3" fill="none"/></svg>
        <span>dkeswick@tidewellhomecraft.co.nz</span>
      </li>
      <li class="contact__item">
        <svg viewBox="0 0 16 16" aria-hidden="true"><circle cx="8" cy="8" r="6.5" fill="#fff"/><path d="M1.5 8h13M8 1.5c-2.4 2.6-2.4 10.4 0 13M8 1.5c2.4 2.6 2.4 10.4 0 13" stroke="var(--green)" stroke-width="1" fill="none"/></svg>
        <span>tidewellhomecraft.co.nz</span>
      </li>
    </ul>

    <div class="holder-name">Dorian Keswick</div>
  </section>

</main>
</body>
</html>
```